Business Card Project for Firm Deck Hoisting

Business name is "Firm Deck Hoisting" we are a scaffolding & rigging business specialising in local and remote work for:
- scaffolding (residential, commercial, industrial)
- rigging
-man material hoists
- swing stages
- labour hire

On the back of the card I would like FDH as the symbol / logo. I have attached the logos we have had created by sketch harbour. We would like to use bold colours – preferably as the same colour scheme as the logo.

Target Market(s)

Construction business

Industry/Entity Type

Construction

Contact Information for Business Card

name: Owen Pellew
Title: Director
Phone: 0491 572 864
Address: PO BOX 3251, Marrowdale SA 5199
Email: owen@firmdeckhoisting.com.au
Website: www.firmdeckhoisting.com.au

Font styles to use
Sans Serif

Requirements
Must have
• Must use existing logo & prefering using bold colours
Nice to have
• Would be nice to have a line of dot points in what we specialise in but not essential
• Would be nice to see some designs with a slogan but not essential
Should not have
• NA

```html
<!DOCTYPE html>
<html lang="en">
<head>
<meta charset="utf-8">
<title>Firm Deck Hoisting – Business Card</title>
<link rel="stylesheet" href="https://fonts.googleapis.com/css2?family=Open+Sans:wght@400;600;700&display=swap">
<style>
  :root {
    --canvas: #ecebe8;
    --brand-blue: #1b78c2;
    --brand-blue-deep: #0e5fa6;
    --brand-blue-light: #3a93d6;
    --ink: #1d1d1f;
    --paper: #ffffff;
    --muted: #3b3b3b;
  }
  * { box-sizing: border-box; margin: 0; padding: 0; }
  html, body {
    width: 1200px; height: 1024px; overflow: hidden;
    background: var(--canvas);
    font-family: "Open Sans", Arial, sans-serif;
  }
  .canvas { position: relative; width: 1200px; height: 1024px; }
  .card {
    position: absolute; left: 250px;
    width: 700px; height: 400px;
    border-radius: 28px; overflow: hidden;
    box-shadow: 0 10px 30px rgba(0,0,0,0.18);
  }
  /* Front */
  .card-front { top: 82px; background: var(--paper); }
  .card-front .edge-band {
    position: absolute; left: 0; right: 0; bottom: 0; height: 22px;
    background: var(--brand-blue);
  }
  .front-mark {
    position: absolute; left: 50px; top: 150px;
    font-size: 92px; font-weight: 700; letter-spacing: 2px;
    color: var(--ink); line-height: 1;
  }
  .divider-vertical {
    position: absolute; left: 305px; top: 60px; width: 2px; height: 240px;
    background: var(--brand-blue);
  }
  .divider-horizontal {
    position: absolute; left: 305px; right: 40px; top: 145px; height: 2px;
    background: var(--brand-blue);
  }
  .identity { position: absolute; left: 330px; top: 62px; }
  .identity .person-name {
    font-size: 26px; font-weight: 600; letter-spacing: 0.5px;
    color: var(--brand-blue); text-transform: uppercase; line-height: 1.2;
  }
  .identity .person-title { font-size: 20px; color: var(--ink); line-height: 1.3; }
  .contact-list { position: absolute; left: 330px; top: 168px; list-style: none; }
  .contact-list li {
    display: flex; align-items: center; gap: 10px;
    font-size: 17px; color: var(--muted); line-height: 30px; white-space: nowrap;
  }
  .contact-list svg { width: 16px; height: 16px; flex: none; fill: var(--brand-blue); }

  /* Back */
  .card-back {
    top: 542px;
    background: linear-gradient(135deg, var(--brand-blue-light) 0%, var(--brand-blue) 45%, var(--brand-blue-deep) 100%);
    color: var(--paper);
  }
  .back-brand {
    position: absolute; left: 50px; top: 50px;
    display: flex; align-items: center; gap: 18px;
  }
  .back-brand .mark { font-size: 72px; font-weight: 700; letter-spacing: 2px; line-height: 1; }
  .back-brand .rule { width: 2px; height: 78px; background: var(--paper); }
  .back-brand .wordmark { font-size: 30px; font-weight: 700; line-height: 1.1; text-transform: uppercase; }
  .services { position: absolute; left: 300px; top: 185px; list-style: none; }
  .services li { position: relative; padding-left: 22px; font-size: 19px; line-height: 30px; }
  .services li::before {
    content: ""; position: absolute; left: 0; top: 11px;
    width: 9px; height: 9px; border-radius: 50%; background: var(--paper);
  }
  .services .note { display: block; line-height: 24px; }
</style>
</head>
<body>
<main class="canvas">
  <section class="card card-front" aria-label="Card front">
    <div class="front-mark">FDH</div>
    <div class="divider-vertical"></div>
    <div class="divider-horizontal"></div>
    <div class="identity">
      <p class="person-name">Owen Pellew</p>
      <p class="person-title">Director</p>
    </div>
    <ul class="contact-list">
      <li>
        <svg viewBox="0 0 24 24" aria-hidden="true"><path d="M6.6 10.8a15.1 15.1 0 0 0 6.6 6.6l2.2-2.2a1 1 0 0 1 1-.25 11.4 11.4 0 0 0 3.6.57 1 1 0 0 1 1 1V20a1 1 0 0 1-1 1A17 17 0 0 1 3 4a1 1 0 0 1 1-1h3.5a1 1 0 0 1 1 1c0 1.25.2 2.45.57 3.57a1 1 0 0 1-.25 1z"/></svg>
        0491 572 864
      </li>
      <li>
        <svg viewBox="0 0 24 24" aria-hidden="true"><path d="M3 5h18v14H3z M3 5l9 7 9-7" fill="none" stroke="#1b78c2" stroke-width="2"/></svg>
        owen@firmdeckhoisting.com.au
      </li>
      <li>
        <svg viewBox="0 0 24 24" aria-hidden="true"><circle cx="12" cy="12" r="9" fill="none" stroke="#1b78c2" stroke-width="2"/><path d="M3 12h18M12 3c3 3 3 15 0 18M12 3c-3 3-3 15 0 18" fill="none" stroke="#1b78c2" stroke-width="1.6"/></svg>
        www.firmdeckhoisting.com.au
      </li>
      <li>
        <svg viewBox="0 0 24 24" aria-hidden="true"><path d="M12 2a7 7 0 0 0-7 7c0 5 7 13 7 13s7-8 7-13a7 7 0 0 0-7-7zm0 9.5A2.5 2.5 0 1 1 12 6.5a2.5 2.5 0 0 1 0 5z"/></svg>
        PO BOX 3251, Marrowdale SA 5199
      </li>
    </ul>
    <div class="edge-band"></div>
  </section>

  <section class="card card-back" aria-label="Card back">
    <div class="back-brand">
      <span class="mark">FDH</span>
      <span class="rule"></span>
      <span class="wordmark">Firm Deck<br>Hoisting</span>
    </div>
    <ul class="services">
      <li>scaffolding<span class="note">(residential, commercial, industrial)</span></li>
      <li>rigging</li>
      <li>man material hoists</li>
      <li>swing stages</li>
      <li>labour hire</li>
    </ul>
  </section>
</main>
</body>
</html>
```